Business Card Design for Toriven

I've already got the logo, but I'd like to see some interesting designs.

I don't want anything to complex. I like it simple,yet innovative, like the logo.

My business is System Administration for small to medium size businesses, so that will be my main target audience.
Updates

hey all, the png has been uploaded.

Hey all,

If you are submitting the back side of the card, I'd like the top bit of the card to be Toriven Solutions and the logo, the bottom of the card the website, with a white background.

The middle I'd like to leave blank for a quote that will be printed on each card.

Thanks!

Dale

Industry/Entity Type

Business

```html
<!DOCTYPE html>
<html lang="en">
<head>
<meta charset="utf-8">
<title>Toriven Solutions – Business Cards</title>
<link rel="stylesheet" href="https://fonts.googleapis.com/css2?family=Arimo:wght@400;700&family=Cormorant+Garamond:ital,wght@1,500&display=swap">
<style>
  :root {
    --stage: #3a3a3a;
    --card: #ffffff;
    --brand-blue: #2b78b6;
    --text-grey: #555555;
    --quote-grey: #6a6a6a;
    --rule-grey: #8a8a8a;
    --wash-blue: #dbe9f3;
  }
  * { margin: 0; padding: 0; box-sizing: border-box; }
  html, body { width: 1200px; height: 900px; overflow: hidden; }
  body {
    background: var(--stage);
    font-family: "Arimo", Arial, sans-serif;
    position: relative;
  }
  .card {
    position: absolute;
    top: 308px;
    width: 514px;
    height: 284px;
    background: var(--card);
    overflow: hidden;
  }
  .card--back { left: 72px; }
  .card--front { left: 615px; }

  .brand {
    position: absolute;
    display: flex;
    align-items: center;
    gap: 12px;
    color: var(--brand-blue);
    font-weight: 700;
    white-space: nowrap;
  }
  .brand__dot {
    border-radius: 50%;
    background: var(--brand-blue);
    flex: none;
  }
  .card--back .brand {
    left: 0; right: 0; top: 44px;
    justify-content: center;
    font-size: 34px;
  }
  .card--back .brand__dot { width: 62px; height: 62px; }

  .quote {
    position: absolute;
    left: 0; right: 0; top: 150px;
    text-align: center;
    font-family: "Cormorant Garamond", Georgia, serif;
    font-style: italic;
    font-weight: 500;
    font-size: 27px;
    line-height: 30px;
    color: var(--quote-grey);
  }
  .website {
    position: absolute;
    left: 0; right: 0; top: 252px;
    text-align: center;
    font-size: 11px;
    color: var(--text-grey);
  }

  .decor-wash {
    position: absolute;
    inset: 0;
    background:
      radial-gradient(ellipse 120px 110px at 120px 20px, var(--wash-blue) 0 70%, transparent 72%),
      radial-gradient(ellipse 150px 150px at 470px 200px, var(--wash-blue) 0 68%, transparent 70%);
    opacity: 0.85;
  }
  .card--front .brand {
    left: 28px; top: 124px;
    font-size: 22px;
    gap: 10px;
  }
  .card--front .brand__dot { width: 48px; height: 48px; }

  .divider {
    position: absolute;
    left: 277px; top: 92px;
    width: 1px; height: 106px;
    background: var(--rule-grey);
  }
  .contact {
    position: absolute;
    left: 297px; top: 92px;
    color: var(--text-grey);
  }
  .contact__name {
    font-size: 19px;
    font-weight: 700;
    color: var(--brand-blue);
    line-height: 24px;
  }
  .contact__role {
    font-size: 13px;
    font-weight: 700;
    margin-top: 2px;
    margin-bottom: 8px;
  }
  .contact__line {
    display: flex;
    align-items: center;
    gap: 8px;
    font-size: 13px;
    line-height: 18px;
  }
  .contact__line--indent { padding-left: 20px; }
  .contact__icon { width: 12px; height: 12px; flex: none; fill: var(--brand-blue); }
</style>
</head>
<body>
  <section class="card card--back" aria-label="Card back">
    <div class="brand"><span class="brand__dot"></span>Toriven Solutions</div>
    <p class="quote">A quote that will<br>be printed on each card</p>
    <p class="website">toriven-solutions.com</p>
  </section>

  <section class="card card--front" aria-label="Card front">
    <div class="decor-wash" role="img" aria-label="Large faint light-blue floral decoration"></div>
    <div class="brand"><span class="brand__dot"></span>Toriven Solutions</div>
    <div class="divider"></div>
    <div class="contact">
      <p class="contact__name">Mark Ellison</p>
      <p class="contact__role">managing director</p>
      <p class="contact__line">
        <svg class="contact__icon" viewBox="0 0 12 12" aria-hidden="true"><path d="M0 2h12v8H0z" /><path d="M0 2l6 4 6-4" fill="none" stroke="#fff" stroke-width="1.2"/></svg>
        48 Harbor Lane
      </p>
      <p class="contact__line contact__line--indent">Milford, Ohio 45150</p>
      <p class="contact__line">
        <svg class="contact__icon" viewBox="0 0 12 12" aria-hidden="true"><rect x="3" y="0" width="6" height="12" rx="1.2"/><rect x="4.2" y="1.6" width="3.6" height="6.5" fill="#fff"/></svg>
        555 014 22 70
      </p>
    </div>
  </section>
</body>
</html>
```